Management Consulting needing a cool business card for client acquisition and networking

We are looking for a business card that is progressive and fresh that conveys innovation, forward thinking, and confidence. The business card is for a company based in Charlotte NC called, 'VELMORE CONSULTING GROUP LLC'. The company primarily works with banks, insurance, and brokerages to implement innovative solutions to help them streamline their operations, to more effectively manage risks, and to improve their customer relationships.

Target Market(s)

Typically meet with Chief Financial Officers, Chief Information Officers, Chief Operations Officer, Business Unit Leader. The target market are generally 40-55 years, male, white, master level education plus.

Industry/Entity Type

Progressive

Font styles to use
Serif
Other font styles liked:
• Calibri

Requirements
Should not have
• Designs that look too much like law firms or accounting companies. Too conservative

```html
<!DOCTYPE html>
<html lang="en">
<head>
<meta charset="utf-8">
<title>Velmore Consulting Group LLC – Business Card</title>
<link rel="stylesheet" href="https://fonts.googleapis.com/css2?family=Cinzel:wght@600&family=Carlito:wght@400;700&display=swap">
<style>
  :root {
    --navy: #1b1f4b;
    --backdrop: #161616;
    --backdrop-light: #2b2b2b;
    --white: #ffffff;
    --silver: #c5c6c8;
    --title-grey: #d9d9dc;
    --ink: #1d1d1f;
    --circle-line: #e4e4e6;
  }
  * { margin: 0; padding: 0; box-sizing: border-box; }
  html, body { width: 1200px; height: 435px; overflow: hidden; }
  body { position: relative; font-family: "Carlito", "Calibri", sans-serif; }

  .backdrop {
    position: absolute; inset: 0;
    background: radial-gradient(ellipse at 50% 40%, var(--backdrop-light), var(--backdrop) 75%);
  }

  .card { position: absolute; border-radius: 22px; overflow: hidden; }

  /* Front */
  .card-front { left: 22px; top: 37px; width: 556px; height: 346px; background: var(--white); }
  .front-shapes { position: absolute; inset: 0; }
  .company-name {
    position: absolute; left: 75px; top: 22px; width: 380px;
    text-align: center; font-family: "Cinzel", serif; font-weight: 600;
    font-size: 27px; line-height: 33px; color: var(--title-grey); letter-spacing: 0.5px;
  }
  .mark-stand {
    position: absolute; left: 440px; top: 58px; width: 80px;
    display: flex; align-items: center; gap: 5px;
    font-family: "Cinzel", serif; font-weight: 600; font-size: 11px; color: var(--title-grey);
  }
  .mark-stand .dot { width: 14px; height: 14px; border: 1.5px solid var(--title-grey); border-radius: 50%; }

  .person { position: absolute; left: 110px; top: 138px; width: 346px; text-align: center; color: var(--ink); }
  .person-name { font-weight: 700; font-size: 21px; line-height: 26px; }
  .person-title { font-size: 14px; line-height: 18px; letter-spacing: 0.3px; }

  .contacts { position: absolute; left: 36px; top: 204px; list-style: none; color: var(--ink); font-size: 14.5px; }
  .contacts li { display: flex; align-items: flex-start; gap: 14px; line-height: 17px; margin-bottom: 7px; }
  .contacts svg { width: 16px; height: 16px; flex: none; margin-top: 1px; }

  /* Back */
  .card-back { left: 620px; top: 63px; width: 552px; height: 344px; background: var(--navy); }
  .back-mark {
    position: absolute; left: 222px; top: 78px; width: 90px; height: 60px;
    display: flex; align-items: center; justify-content: center;
  }
  .back-mark .dot { width: 56px; height: 56px; border: 1.5px solid var(--silver); border-radius: 50%; }
  .back-name {
    position: absolute; left: 0; right: 0; top: 150px; text-align: center;
    font-family: "Cinzel", serif; font-weight: 600; font-size: 23px; color: var(--title-grey); letter-spacing: 0.4px;
  }
  .back-url { position: absolute; right: 68px; top: 184px; font-size: 12px; color: var(--white); letter-spacing: 0.3px; }
</style>
</head>
<body>
  <div class="backdrop" role="img" aria-label="Dark damask patterned backdrop"></div>

  <section class="card card-front">
    <svg class="front-shapes" viewBox="0 0 556 346" aria-hidden="true">
      <polygon points="0,0 556,0 556,128 0,128" fill="var(--navy)"/>
      <polygon points="0,0 38,0 60,64 0,128" fill="var(--white)"/>
      <circle cx="440" cy="255" r="76" fill="none" stroke="var(--circle-line)" stroke-width="2"/>
    </svg>
    <h1 class="company-name">Velmore Consulting<br>Group LLC</h1>
    <div class="mark-stand"><span class="dot"></span>VELMORE</div>

    <div class="person">
      <p class="person-name">Marcus T. Lorne</p>
      <p class="person-title">CHIEF SOLUTIONS ARCHITECT</p>
    </div>

    <ul class="contacts">
      <li><svg viewBox="0 0 16 16"><path d="M3 1h3l1 4-2 1.5c1 2 2.5 3.5 4.5 4.5L11 9l4 1v3c0 1-1 2-2 2C7 15 1 9 1 3c0-1 1-2 2-2z" fill="var(--ink)"/></svg>704.555.0142</li>
      <li><svg viewBox="0 0 16 16"><rect x="4" y="1" width="8" height="14" rx="1.5" fill="var(--ink)"/><rect x="5.5" y="3" width="5" height="5" fill="var(--white)"/></svg>704.555.0187</li>
      <li><svg viewBox="0 0 16 16"><path d="M1 6l7-5 7 5v9H1z" fill="var(--ink)"/><path d="M1 6l7 5 7-5" stroke="var(--white)" stroke-width="1.2" fill="none"/></svg>mlorne@velmoreconsulting.com</li>
      <li><svg viewBox="0 0 16 16"><circle cx="8" cy="8" r="7" fill="var(--ink)"/><circle cx="8" cy="8" r="4" fill="none" stroke="var(--white)" stroke-width="1.2"/><path d="M4 8h8M8 4v8" stroke="var(--white)" stroke-width="1"/></svg>www.velmoreconsulting.com</li>
      <li><svg viewBox="0 0 16 16"><rect x="1" y="3" width="14" height="10" fill="var(--ink)"/><path d="M1 3l7 6 7-6" stroke="var(--white)" stroke-width="1.2" fill="none"/></svg><span>1875 Brookline rd., Suite 300<br>Charlotte, NC 28209</span></li>
    </ul>
  </section>

  <section class="card card-back">
    <div class="back-mark"><span class="dot"></span></div>
    <h2 class="back-name">Velmore Consulting Group LLC</h2>
    <p class="back-url">www.velmoreconsulting.com</p>
  </section>
</body>
</html>
```